Business Card, Stationary with Shark Logo for Personal Injury Lawyer

I need business cards and stationery with a shark logo for my Personal Injury Law Practice. Has to have this written on it:
Martin K. Hollis
Injury Lawyer
The Corvell Building
718 Tandy Street
Providence, Rhode Island 02908
401-627-4193
Martinhollis.com

Contact Information for Business Card

Martin K. Hollis, Injury Lawyer, address, 401-627-4193, martinhollis.com

```html
<!DOCTYPE html>
<html lang="en">
<head>
<meta charset="utf-8">
<title>Martin K. Hollis – Business Card</title>
<link rel="stylesheet" href="https://fonts.googleapis.com/css2?family=Montserrat:wght@400;500;800&display=swap">
<style>
  :root {
    --page-bg: #e4e1dc;
    --card-navy: #2f2b78;
    --card-navy-deep: #1e1c5a;
    --frost: #eef0f2;
    --frost-edge: #c9c6c0;
    --ink-light: #ece4d2;
    --logo-navy: #1d1f66;
  }
  * { box-sizing: border-box; margin: 0; padding: 0; }
  html, body {
    width: 1200px; height: 887px; overflow: hidden;
    background: var(--page-bg);
  }
  .card {
    position: absolute; left: 100px; top: 173px;
    width: 1000px; height: 540px;
    border-radius: 26px; overflow: hidden;
    box-shadow: 0 10px 30px rgba(0,0,0,0.18);
  }
  .card-shape { position: absolute; inset: 0; }
  .details {
    position: absolute; left: 62px; top: 108px;
    font-family: "Montserrat", sans-serif; color: var(--ink-light);
  }
  .details .name { font-size: 32px; font-weight: 500; letter-spacing: 0.5px; }
  .details .role { font-size: 22px; font-weight: 400; letter-spacing: 1px; margin-top: 4px; }
  .details .building { font-size: 22px; font-weight: 500; letter-spacing: 0.6px; margin-top: 46px; }
  .details .address { font-size: 22px; font-weight: 400; letter-spacing: 1.2px; line-height: 32px; margin-top: 4px; }
  .contacts { list-style: none; margin-top: 36px; font-size: 22px; letter-spacing: 0.8px; line-height: 32px; }
  .contacts li { display: flex; align-items: center; gap: 10px; }
  .contacts svg { width: 18px; height: 18px; flex: none; }
  .brand {
    position: absolute; left: 560px; top: 0; width: 420px; height: 540px;
    display: flex; align-items: center; justify-content: center;
    font-family: "Montserrat", sans-serif; font-weight: 800;
    color: var(--logo-navy); font-size: 44px; text-transform: uppercase;
    letter-spacing: 1px; text-align: center; line-height: 1.1;
  }
</style>
</head>
<body>
  <div class="card">
    <svg class="card-shape" viewBox="0 0 1000 540" aria-hidden="true">
      <defs>
        <linearGradient id="navyFill" x1="0" y1="0" x2="0" y2="1">
          <stop offset="0" stop-color="var(--card-navy)"/>
          <stop offset="1" stop-color="var(--card-navy-deep)"/>
        </linearGradient>
      </defs>
      <rect width="1000" height="540" fill="url(#navyFill)"/>
      <circle cx="730" cy="270" r="271" fill="var(--frost-edge)"/>
      <rect x="741" y="0" width="259" height="540" fill="var(--frost)"/>
      <circle cx="741" cy="270" r="271" fill="var(--frost)"/>
    </svg>

    <div class="details">
      <p class="name">MARTIN K. HOLLIS</p>
      <p class="role">INJURY LAWYER</p>
      <p class="building">THE CORVELL BUILDING</p>
      <p class="address">718 Tandy Street Providence,<br>Rhode Island 02908</p>
      <ul class="contacts">
        <li>
          <svg viewBox="0 0 24 24"><path fill="currentColor" d="M6.6 10.8a15 15 0 0 0 6.6 6.6l2.2-2.2a1 1 0 0 1 1-.25 11.4 11.4 0 0 0 3.6.57 1 1 0 0 1 1 1V20a1 1 0 0 1-1 1A17 17 0 0 1 3 4a1 1 0 0 1 1-1h3.5a1 1 0 0 1 1 1c0 1.25.2 2.45.57 3.57a1 1 0 0 1-.25 1z"/></svg>
          401-627-4193
        </li>
        <li>
          <svg viewBox="0 0 24 24"><rect x="3" y="6" width="18" height="12" rx="1" fill="none" stroke="currentColor" stroke-width="2"/><path d="M3 7l9 6 9-6" fill="none" stroke="currentColor" stroke-width="2"/></svg>
          info@martinhollis.com
        </li>
        <li>
          <svg viewBox="0 0 24 24" fill="none" stroke="currentColor" stroke-width="1.8"><circle cx="12" cy="12" r="9"/><ellipse cx="12" cy="12" rx="4" ry="9"/><path d="M3 12h18M5 7h14M5 17h14"/></svg>
          www.martinhollis.com
        </li>
      </ul>
    </div>

    <div class="brand">Martin K.<br>Hollis</div>
  </div>
</body>
</html>
```